Industrial Automation company requires a business card design

Dravel Automation provides design & build of Automated Equipment for manufacturing industry.
www.dravelautomation-example.com
The equipment we design is used for manufacturing in sectors such as medical device, pharmaceutical, aerospace and electronics.
We require a new business card design which incorporates our (New) logo and the key message words:
Automated Equipment:
Design, Build, Control, Test, Support

```html
<!DOCTYPE html>
<html lang="en">
<head>
<meta charset="utf-8">
<title>Dravel Automation – Business Card</title>
<link rel="stylesheet" href="https://fonts.googleapis.com/css2?family=Open+Sans:wght@400;600;700&display=swap">
<style>
  :root {
    --brand-green: #0f7d3e;
    --brand-green-dark: #0b6b34;
    --ink: #2b2b2b;
    --ink-soft: #3c3c3c;
    --card-white: #ffffff;
    --card-mist: #ececec;
    --backdrop: #3a3a3a;
    --on-green: #ffffff;
  }
  * { margin: 0; padding: 0; box-sizing: border-box; }
  html, body {
    width: 1200px; height: 848px; overflow: hidden;
    background: var(--backdrop);
    font-family: "Open Sans", Arial, sans-serif;
  }
  .canvas { position: relative; width: 1200px; height: 848px; }

  .card {
    position: absolute; left: 360px; width: 486px; height: 276px;
    border-radius: 17px; overflow: hidden;
  }
  .card--front {
    top: 134px;
    background: radial-gradient(ellipse at 45% 30%, var(--card-white) 40%, var(--card-mist) 100%);
  }
  .card--back { top: 451px; background: var(--brand-green); }

  .wordmark {
    position: absolute; left: 36px;
    display: flex; align-items: center; gap: 10px;
    font-weight: 700; font-size: 25px; letter-spacing: 2px;
    text-transform: uppercase; line-height: 1; white-space: nowrap;
  }
  .wordmark__dot { width: 20px; height: 20px; border-radius: 50%; flex: none; }
  .card--front .wordmark { top: 42px; color: var(--brand-green); }
  .card--front .wordmark__dot { background: var(--brand-green); }
  .card--back .wordmark { top: 153px; color: var(--on-green); }
  .card--back .wordmark__dot { background: var(--on-green); }

  .person { position: absolute; left: 36px; top: 146px; width: 298px; }
  .person__name {
    font-weight: 700; font-size: 13.5px; color: var(--brand-green);
    letter-spacing: 0.2px;
  }
  .person__role { font-size: 12px; color: var(--ink-soft); margin-top: 1px; }
  .person__rule { height: 1px; background: var(--brand-green); margin-top: 6px; }

  .contact-list, .address {
    position: absolute; top: 196px; list-style: none;
    font-size: 10.5px; color: var(--ink); line-height: 15.5px; white-space: nowrap;
  }
  .contact-list { left: 36px; }
  .contact-list li, .address { display: flex; align-items: flex-start; gap: 5px; }
  .contact-list svg, .address svg { width: 9px; height: 9px; margin-top: 3px; flex: none; fill: var(--brand-green); color: var(--brand-green); }
  .address { left: 212px; }

  .accent-strip { position: absolute; right: 0; bottom: 0; width: 180px; height: 14px; }

  .tagline {
    position: absolute; left: 36px; top: 224px;
    font-weight: 700; font-size: 12.5px; line-height: 17px; color: var(--on-green);
  }
</style>
</head>
<body>
<main class="canvas">
  <section class="card card--front" aria-label="Business card front">
    <div class="wordmark"><span class="wordmark__dot"></span>Dravel Automation</div>

    <div class="person">
      <p class="person__name">MARCUS LANE HOLLIS</p>
      <p class="person__role">Chairman</p>
      <div class="person__rule"></div>
    </div>

    <ul class="contact-list">
      <li><svg viewBox="0 0 10 10"><path d="M2 0l2 2-1 1.5c.6 1.4 2 2.8 3.5 3.5L8 6l2 2-1.5 2C4 9.5.5 6 0 1.5z"/></svg>(555) 013-4720</li>
      <li><svg viewBox="0 0 10 10"><rect x="2.5" y="0" width="5" height="10" rx="1"/></svg>(555) 013-4721</li>
      <li><svg viewBox="0 0 10 10"><circle cx="5" cy="5" r="4.5" fill="none" stroke="currentColor"/><circle cx="5" cy="5" r="2"/></svg>sales@corvane-example.com</li>
      <li><svg viewBox="0 0 10 10"><circle cx="5" cy="5" r="5"/></svg>www.corvane-example.com</li>
    </ul>

    <div class="address">
      <svg viewBox="0 0 10 10"><path d="M5 0a3.5 3.5 0 0 1 3.5 3.5C8.5 6 5 10 5 10S1.5 6 1.5 3.5A3.5 3.5 0 0 1 5 0zm0 2a1.5 1.5 0 1 0 0 3 1.5 1.5 0 0 0 0-3z"/></svg>
      <p>Corvane Technologies<br>2750 Ridgeway St<br>Riverton, Texas 77000</p>
    </div>

    <svg class="accent-strip" viewBox="0 0 180 14" preserveAspectRatio="none" aria-hidden="true">
      <polygon points="12,0 180,0 180,14 0,14" fill="var(--brand-green)"/>
    </svg>
  </section>

  <section class="card card--back" aria-label="Business card back">
    <div class="wordmark"><span class="wordmark__dot"></span>Dravel Automation</div>
    <p class="tagline">Automated Equipment:<br>Design, Build, Control, Test, Support</p>
  </section>
</main>
</body>
</html>
```